Mend Your Frame
Stationary
Project: Mend Your Frame
Mend Your Frame - Health
Creative Brief
Use specific fonts
Whatever fonts look best!
Professional
Dellan Corvin
Body Composition Specialist/ Personal Trainer
Dont put address.
dellcorvin@mailnest.example
MendYourFrameAnalysis.example
We use a state of the art body composition analyzer to accurately determine total body fat, essential fat, non essential fat, reserve fat, total body water, and lean mass. It's fast, non-invasive, and comparable to the Gold Standard. To find out more visit our website or call us.

```html
<!DOCTYPE html>
<html lang="en">
<head>
<meta charset="utf-8">
<title>Mend Your Frame — Stationery</title>
<link rel="stylesheet" href="https://fonts.googleapis.com/css2?family=Oswald:wght@700&family=Arimo:wght@400;700&display=swap">
<style>
:root{
  --bg-light:#5fa0e6;
  --bg-mid:#1f5fc4;
  --bg-deep:#06245e;
  --navy:#0a1a3a;
  --ink:#1b2d4f;
  --brand-blue:#2f7fd6;
  --paper:#ffffff;
  --label:#d8e8ff;
}
*{box-sizing:border-box;margin:0;padding:0}
html,body{width:1200px;height:862px;overflow:hidden}
body{
  position:relative;
  font-family:"Arimo",Arial,sans-serif;
  background:radial-gradient(ellipse at 45% 0%,var(--bg-light) 0%,var(--bg-mid) 45%,var(--bg-deep) 100%);
}
.label{position:absolute;color:var(--label);font-size:11px;letter-spacing:.2px}
.brand{font-family:"Oswald",Impact,sans-serif;font-weight:700;text-transform:uppercase;color:var(--brand-blue);line-height:1;white-space:nowrap}
.tagline{font-size:7px;color:var(--brand-blue);line-height:1.15}
.web{font-weight:700;color:var(--ink);font-size:7px;white-space:nowrap}
.contact{color:var(--ink);font-size:6px;line-height:1.5}

/* envelope front */
.envelope-front{position:absolute;left:24px;top:40px;width:307px;height:248px;background:var(--paper);box-shadow:0 3px 10px rgba(0,0,0,.25)}
.envelope-front .brand{position:absolute;left:16px;top:14px;font-size:22px}
.envelope-front .tagline{position:absolute;left:16px;top:42px}
.envelope-front .window{position:absolute;left:44px;top:120px;width:176px;height:58px;background:#e4e6ea;border:1px solid #d0d3d8}
.envelope-front .contact{position:absolute;left:10px;top:200px;transform:rotate(-90deg);transform-origin:left top;white-space:nowrap}
.envelope-front .web{position:absolute;left:40px;top:232px}

/* envelope back */
.envelope-back{position:absolute;left:355px;top:64px;width:437px;height:220px;background:var(--paper);box-shadow:0 3px 10px rgba(0,0,0,.25)}
.envelope-back svg{position:absolute;left:0;top:0}
.envelope-back .web{position:absolute;left:0;right:0;top:160px;text-align:center}

/* folder */
.folder{position:absolute;left:46px;top:376px;width:424px;height:392px}
.folder svg{position:absolute;left:0;top:0}
.folder .brand-vertical{position:absolute;left:20px;top:222px;transform:rotate(-90deg);transform-origin:left top;font-size:30px}
.folder .web-vertical{position:absolute;left:60px;top:212px;transform:rotate(-90deg);transform-origin:left top;font-size:8px;font-weight:700;color:var(--ink);white-space:nowrap}
.folder .pitch{position:absolute;left:40px;top:265px;width:280px;color:#fff;font-weight:700;font-size:11px;line-height:1.27;transform:rotate(-14deg);transform-origin:left top}

/* letterhead */
.letterhead{position:absolute;left:470px;top:312px;width:310px;height:456px;background:var(--paper);box-shadow:0 3px 10px rgba(0,0,0,.25)}
.letterhead .brand{position:absolute;left:16px;top:14px;font-size:20px}
.letterhead .tagline{position:absolute;left:16px;top:40px}
.letterhead .contact{position:absolute;left:10px;top:430px;transform:rotate(-90deg);transform-origin:left top;white-space:nowrap}
.letterhead .web{position:absolute;left:0;right:0;bottom:14px;text-align:center}

/* business cards */
.card{position:absolute;left:888px;width:293px;height:144px;border-radius:6px;overflow:hidden;box-shadow:0 3px 10px rgba(0,0,0,.35);
  background:linear-gradient(135deg,#0b1733 0%,#133a7a 55%,#0b1733 100%)}
.card-front{top:360px}
.card-front .brand{position:absolute;left:14px;top:14px;font-size:24px;color:#8fc3ff}
.card-front .tagline{position:absolute;left:14px;top:44px;color:#8fc3ff}
.card-front .name{position:absolute;left:112px;top:72px;color:#fff;font-weight:700;font-size:11px;padding-left:6px;border-left:1px solid #8fc3ff}
.card-front .title{position:absolute;left:118px;top:86px;color:#cfe0f5;font-size:6px}
.card-front .contact{position:absolute;left:14px;top:118px;color:#cfe0f5;font-size:6px}
.card-front .web{position:absolute;right:14px;top:118px;color:#fff;font-size:6.5px}
.card-back{top:564px}
.card-back p{position:absolute;left:16px;top:16px;width:262px;color:#fff;font-weight:700;font-size:10px;line-height:1.3}
</style>
</head>
<body>

<span class="label" style="left:112px;top:22px">Envelope Front</span>
<span class="label" style="left:540px;top:42px">Envelope Front</span>
<span class="label" style="left:940px;top:338px">Business card- FRONT</span>
<span class="label" style="left:948px;top:716px">Business card- BACK</span>
<span class="label" style="left:96px;top:776px">FOLDER</span>
<span class="label" style="left:598px;top:778px">Letterhead</span>

<section class="envelope-front">
  <div class="brand">Mend Your Frame</div>
  <div class="tagline">Look great.<br>Feel great.<br>Do great things.</div>
  <div class="window"></div>
  <div class="contact">P: 555.010.2468<br>dellcorvin@mailnest.example</div>
  <div class="web">MendYourFrameAnalysis.example</div>
</section>

<section class="envelope-back">
  <svg width="437" height="220" viewBox="0 0 437 220" aria-hidden="true">
    <defs>
      <linearGradient id="flap" x1="0" y1="0" x2="0" y2="1">
        <stop offset="0" stop-color="#0a1a3a"/>
        <stop offset="1" stop-color="#2a6fd0"/>
      </linearGradient>
    </defs>
    <path d="M0 0H437V40L240 86Q218 92 196 86L0 40Z" fill="url(#flap)"/>
  </svg>
  <div class="web">MendYourFrameAnalysis.example</div>
</section>

<section class="folder">
  <svg width="424" height="392" viewBox="0 0 424 392">
    <defs>
      <linearGradient id="back-panel" x1="0" y1="0" x2="1" y2="1">
        <stop offset="0" stop-color="#f4f5f7"/>
        <stop offset=".5" stop-color="#b9bec6"/>
        <stop offset="1" stop-color="#eef0f3"/>
      </linearGradient>
      <radialGradient id="swirl" cx=".6" cy=".3" r=".7">
        <stop offset="0" stop-color="#ffffff"/>
        <stop offset="1" stop-color="#cfdff5"/>
      </radialGradient>
      <linearGradient id="pocket" x1="0" y1="0" x2="1" y2="1">
        <stop offset="0" stop-color="#0a1a3a"/>
        <stop offset=".6" stop-color="#143e86"/>
        <stop offset="1" stop-color="#2a6fd0"/>
      </linearGradient>
    </defs>
    <path d="M180 0H424V392H180Z" fill="url(#back-panel)"/>
    <path d="M0 30L200 0L380 80V392H0Z" fill="url(#swirl)" role="img" aria-label="Light blue flowing line pattern on folder cover"/>
    <path d="M0 260Q150 150 380 170V392H0Z" fill="url(#pocket)"/>
  </svg>
  <div class="brand brand-vertical">Mend Your Frame</div>
  <div class="web-vertical">MendYourFrameAnalysis.example</div>
  <p class="pitch">We use a state of the art body composition analyzer to accurately determine total body fat, essential fat, non essential fat, reserve fat, total body water, and lean mass. It's fast, non-invasive, and comparable to the Gold Standard. To find out more visit our website or call us.</p>
</section>

<section class="letterhead">
  <div class="brand">Mend Your Frame</div>
  <div class="tagline">Look great.<br>Feel great.<br>Do great things.</div>
  <div class="contact">P: 555.010.2468<br>dellcorvin@mailnest.example</div>
  <div class="web">MendYourFrameAnalysis.example</div>
</section>

<section class="card card-front">
  <div class="brand">Mend Your Frame</div>
  <div class="tagline">Look great.<br>Feel great.<br>Do great things.</div>
  <div class="name">Dellan Corvin</div>
  <div class="title">Body Composition Specialist/ Personal Trainer</div>
  <div class="contact">P: 555.010.2468 · dellcorvin@mailnest.example</div>
  <div class="web">MendYourFrameAnalysis.example</div>
</section>

<section class="card card-back">
  <p>We use a state of the art body composition analyzer to accurately determine total body fat, essential fat, non essential fat, reserve fat, total body water, and lean mass. It's fast, non-invasive, and comparable to the Gold Standard. To find out more visit our website or call us.</p>
</section>

</body>
</html>
```